Ridgeline Outfitters Business Cards

Recently had a logo done with Artfolio and now looking for a business card to go along with it.

Target Market(s)

Ridgeline Outfitters is a weapons dealer. My market will be primarily men, hunting, shooting type.

Industry/Entity Type

Business

Contact Information for Business Card

I selected double sided, but this is not required, single or double is going to be fine. I picture the logo on one side, or perhaps just the circle which contains "RO" with the remaining info on the other side.

Font styles to use
Sans Serif

Requirements
Must have
• My name: Milo Brandt
• Title: Owner
• tel: 612-555-0187
• web: www.ridgelineoutfittersmn.example
Nice to have
• I like the concept of a black business card. I would like to keep the colors monotone, black, grey, white or red. Red is acceptable because it is in the logo. I have also seen cards that are matte black with shiny black as well, perhaps for the logo (or circle RO) part of the logo.
• I will upload a couple of the logos for use, and also an example I just found of the black on black. and some others that have a nice contrast.
Should not have
• lots of colors are not wanted.

```html
<!DOCTYPE html>
<html lang="en">
<head>
<meta charset="utf-8">
<title>Ridgeline Outfitters – Business Card Concepts</title>
<link rel="stylesheet" href="https://fonts.googleapis.com/css2?family=Montserrat:wght@400;500;800&family=Zilla+Slab:wght@600;700&display=swap">
<style>
  :root {
    --page: #ffffff;
    --frame: #b4b4b4;
    --card: #464648;
    --ink: #111112;
    --heading: #3a3a3a;
  }
  * { margin: 0; padding: 0; box-sizing: border-box; }
  html, body { width: 1200px; height: 960px; overflow: hidden; background: var(--page); }
  .sheet { position: relative; width: 1200px; height: 960px; }

  .group-frame { position: absolute; left: 13px; top: 20px; width: 453px; height: 920px; border: 2px solid var(--frame); }

  .design-title, .design-note, .side-label {
    position: absolute; font-family: "Zilla Slab", Georgia, serif; color: var(--heading); text-align: center;
  }
  .design-title { font-size: 26px; font-weight: 700; letter-spacing: .02em; line-height: 1; }
  .design-note { font-size: 10.5px; font-weight: 700; line-height: 1.3; text-transform: uppercase; letter-spacing: .01em; color: #1c1c1c; }
  .side-label { font-size: 14px; font-weight: 700; text-align: right; width: 120px; }

  .card { position: absolute; width: 419px; height: 239px; background: var(--card); font-family: "Montserrat", Arial, sans-serif; color: var(--ink); overflow: hidden; }
  .card--tall { width: 240px; height: 419px; }

  .mark-ring { position: absolute; border: 6px solid var(--ink); border-radius: 50%; }
  .mark-ring--large { border-width: 9px; }

  .wordmark { position: absolute; font-weight: 800; text-transform: uppercase; letter-spacing: .05em; line-height: 1.05; color: var(--ink); }

  .contact { position: absolute; line-height: 1.25; }
  .contact .name { font-size: 16px; font-weight: 500; letter-spacing: .03em; }
  .contact .role { font-size: 10.5px; font-weight: 500; letter-spacing: .04em; margin-bottom: 14px; }
  .contact .line { font-size: 12px; letter-spacing: .04em; white-space: nowrap; }
  .contact--center { text-align: center; left: 0; right: 0; }
  .contact--slab { font-family: "Zilla Slab", Georgia, serif; }
  .contact--slab .name { font-weight: 700; font-size: 15px; }
  .contact--slab .role { font-weight: 700; font-size: 9.5px; }
  .contact--slab .line { font-size: 10px; letter-spacing: .02em; }
  .contact--narrow .line { font-size: 10px; letter-spacing: .02em; }
</style>
</head>
<body>
<main class="sheet">

  <!-- Design 1: double sided -->
  <div class="group-frame"></div>
  <h2 class="design-title" style="left:13px;width:453px;top:36px;">DESIGN #1</h2>
  <p class="design-note" style="left:13px;width:453px;top:66px;">Double sided, shiny black print on matte black paper</p>

  <section class="card" style="left:29px;top:98px;">
    <div class="mark-ring mark-ring--large" style="left:148px;top:58px;width:123px;height:123px;"></div>
    <div class="wordmark" style="left:148px;top:106px;width:123px;text-align:center;font-size:11px;">Ridgeline<br>Outfitters</div>
  </section>
  <p class="side-label" style="left:326px;top:338px;">BACK</p>

  <section class="card" style="left:30px;top:385px;">
    <div class="wordmark" style="left:36px;top:44px;font-size:21px;">Ridgeline<br>Outfitters</div>
    <div class="contact" style="left:38px;top:118px;">
      <p class="name">Milo Brandt</p>
      <p class="role">Owner</p>
      <p class="line">(612) 555 0187</p>
      <p class="line">www.ridgelineoutfittersmn.example</p>
    </div>
  </section>
  <p class="side-label" style="left:326px;top:626px;">FRONT A</p>

  <section class="card" style="left:30px;top:665px;">
    <div class="wordmark" style="left:0;right:0;text-align:center;top:46px;font-size:20px;">Ridgeline<br>Outfitters</div>
    <div class="contact contact--center" style="top:113px;">
      <p class="name">Milo Brandt</p>
      <p class="role">Owner</p>
      <p class="line">(612) 555 0187</p>
      <p class="line">www.ridgelineoutfittersmn.example</p>
    </div>
  </section>

  <!-- Design 2 -->
  <h2 class="design-title" style="left:493px;width:419px;top:37px;">DESIGN #2</h2>
  <p class="design-note" style="left:470px;width:465px;top:64px;">One sided, shiny black print on matte black paper</p>
  <section class="card" style="left:494px;top:82px;">
    <div class="mark-ring" style="left:29px;top:36px;width:66px;height:66px;"></div>
    <div class="wordmark" style="left:108px;top:53px;font-size:15px;">Ridgeline<br>Outfitters</div>
    <div class="contact" style="left:37px;top:130px;">
      <p class="name">Milo Brandt</p>
      <p class="role">Owner</p>
      <p class="line">(612) 555 0187</p>
      <p class="line">www.ridgelineoutfittersmn.example</p>
    </div>
  </section>

  <!-- Design 3 -->
  <h2 class="design-title" style="left:493px;width:419px;top:346px;">DESIGN #3</h2>
  <p class="design-note" style="left:470px;width:465px;top:374px;">One sided, shiny black print on matte black paper</p>
  <section class="card" style="left:494px;top:390px;">
    <div class="mark-ring" style="left:13px;top:40px;width:75px;height:75px;"></div>
    <div class="wordmark" style="left:106px;top:62px;font-size:17px;">Ridgeline<br>Outfitters</div>
    <div class="contact" style="left:106px;top:126px;">
      <p class="name">Milo Brandt</p>
      <p class="role">Owner</p>
      <p class="line">(612) 555 0187</p>
      <p class="line">www.ridgelineoutfittersmn.example</p>
    </div>
  </section>

  <!-- Design 3, alternate -->
  <h2 class="design-title" style="left:498px;width:420px;top:647px;">DESIGN #3</h2>
  <p class="design-note" style="left:475px;width:465px;top:676px;">One sided, shiny black print on matte black paper</p>
  <section class="card" style="left:499px;top:690px;">
    <div class="mark-ring mark-ring--large" style="left:18px;top:42px;width:151px;height:151px;"></div>
    <div class="wordmark" style="left:226px;top:42px;font-size:15px;">Ridgeline<br>Outfitters</div>
    <div class="contact contact--slab" style="left:226px;top:124px;">
      <p class="name">Milo Brandt</p>
      <p class="role">Owner</p>
      <p class="line">(612) 555 0187</p>
      <p class="line">www.ridgelineoutfittersmn.example</p>
    </div>
  </section>

  <!-- Design 5 -->
  <h2 class="design-title" style="left:947px;width:240px;top:37px;">DESIGN #5</h2>
  <p class="design-note" style="left:947px;width:240px;top:69px;">One sided, shiny black print<br>on matte black paper</p>
  <section class="card card--tall" style="left:947px;top:99px;">
    <div class="mark-ring" style="left:21px;top:47px;width:90px;height:90px;"></div>
    <div class="wordmark" style="left:22px;top:146px;font-size:19px;">Ridgeline<br>Outfitters</div>
    <div class="contact contact--narrow" style="left:26px;top:286px;">
      <p class="name">Milo Brandt</p>
      <p class="role">Owner</p>
      <p class="line">(612) 555 0187</p>
      <p class="line">www.ridgelineoutfittersmn.example</p>
    </div>
  </section>

</main>
</body>
</html>
```